Wine Label for a Prosecco Wine Called Vuro

Prosecco is a white sparkling wine from Italy. We are looking for an eye catching, elegant label for this prosecco that is called "Vuro" because it is a young, fresh, lively white sparkling wine. (We do not want to see children or babies featured on the label-- just the name VURO please.) Attached is the old label for your reference, and the bottle type that will be used , which is a dark green Burgundy style bottle (pls ignore the label on the bottle). Please no grapes or wine glasses on the label. We are looking for something: eye catching / fun / ELEGANT (not cheap). We would be happy with a fun color too. Remember-- elegant, eye catching! Thanks!
Updates

Hi All, I think I made a mistake in my brief and have updated it. I also uploaded a competitor's label that we like very much to give better direction to what we are looking for. Also, the word Vuro cannot be vertical, nor can it be broken. It needs to read: VURO or Vuro. Thanks

Target Market(s)

American adults male and female.

Colors
abd036
33a6d7
33b8a4
ffcf3e

Requirements
Must have
• The mandatory information as shown on old labels. The word VURO should be very prominent.
Nice to have
• The uploaded photo of a competitor's prosecco shows a label we really like... if you could play around with this shape and style we'd be very happy.
Should not have
• No grape images, no wine glass images, no images of babies or children.

```html
<!DOCTYPE html>
<html lang="en">
<head>
<meta charset="UTF-8">
<title>Vuro Prosecco Frizzante – Label</title>
<link rel="stylesheet" href="https://fonts.googleapis.com/css2?family=Didact+Gothic&family=Tinos&display=swap">
<style>
  :root {
    --canvas-bg: #ffffff;
    --label-gold: #c8a676;
    --label-ink: #ffffff;
  }
  * { margin: 0; padding: 0; box-sizing: border-box; }
  html, body {
    width: 1200px;
    height: 1190px;
    overflow: hidden;
    background: var(--canvas-bg);
  }
  .canvas {
    position: relative;
    width: 1200px;
    height: 1190px;
  }
  .wine-label {
    position: absolute;
    left: 339px;
    top: 295px;
    width: 522px;
    height: 600px;
    background: var(--label-gold);
    color: var(--label-ink);
    text-align: center;
  }
  .wine-label > * {
    position: absolute;
    left: 0;
    right: 0;
    line-height: 1;
    white-space: nowrap;
  }
  .brand-name {
    top: 218px;
    font-family: "Didact Gothic", "Century Gothic", sans-serif;
    font-size: 152px;
    letter-spacing: 2px;
  }
  .wine-type {
    top: 452px;
    font-family: "Tinos", "Times New Roman", serif;
    font-size: 28px;
  }
  .appellation {
    top: 492px;
    font-family: "Tinos", "Times New Roman", serif;
    font-size: 20px;
  }
  .region {
    top: 528px;
    font-family: "Tinos", "Times New Roman", serif;
    font-size: 33px;
  }
</style>
</head>
<body>
  <main class="canvas">
    <section class="wine-label">
      <h1 class="brand-name">vuro</h1>
      <p class="wine-type">PROSECCO FRIZZANTE</p>
      <p class="appellation">INDICAZIONE GEOGRAFICA TIPICA</p>
      <p class="region">VENETO</p>
    </section>
  </main>
</body>
</html>
```